Velorant Jobs portal

Velorant Jobs is a job portal connecting job seekers and companies offering part time jobs in the Mena region, starting in the UAE. We would like to see designs that use the color blue. We have attached images to give an idea what the website should look like. When a company posts a job the job seekers are not allowed to see which company has posted a job. There should also be a quidnest gateway. On the landing page we want a catching picture that we will send.

Target Market(s)

Students and promotional workers

Logo Text

Velorant Jobs

Coding

Coded - Design and coding required

Number of Pages Required

4 page

Font styles to use
Sans Serif

Colors
33a6d7
0692cd
85cae6

```html
<!DOCTYPE html>
<html lang="en">
<head>
<meta charset="utf-8">
<title>Velorant Jobs – Job Listings</title>
<link href="https://fonts.googleapis.com/css2?family=Open+Sans:wght@400;600&display=swap" rel="stylesheet">
<style>
:root{
  --teal:#4fc1c6;
  --purple:#7b3f9e;
  --blue:#2b5aa8;
  --stripe-blue:#3a5fa8;
  --stripe-pink:#e0457b;
  --bg:#f4f4f4;
  --panel:#ffffff;
  --text:#555555;
  --text-dark:#444444;
  --line:#e8e8e8;
  --muted:#999999;
}
*{box-sizing:border-box;margin:0;padding:0}
html,body{width:1200px;height:900px;overflow:hidden}
body{background:var(--bg);font-family:"Open Sans",sans-serif;color:var(--text);position:relative}
.top-stripe{position:absolute;top:0;left:0;width:1200px;height:3px;display:flex}
.top-stripe span{flex:1}
.site-header{position:absolute;top:0;left:0;width:1200px;height:82px;background:var(--panel);box-shadow:0 1px 4px rgba(0,0,0,.05)}
.brand{position:absolute;left:99px;top:20px;font-size:34px;color:var(--teal);letter-spacing:-.5px;font-weight:400}
.brand b{color:var(--stripe-blue);font-weight:400}
.main-nav{position:absolute;left:323px;top:36px;font-size:13px;color:var(--text-dark)}
.main-nav .sep{margin:0 14px}
.user-tools{position:absolute;right:99px;top:26px;display:flex;align-items:center;gap:18px}
.bell{position:relative}
.badge{position:absolute;top:-8px;left:8px;width:20px;height:20px;border-radius:50%;background:var(--stripe-blue);color:#fff;font-size:9px;display:flex;align-items:center;justify-content:center;border:2px solid #fff}
.avatar{width:42px;height:42px;border-radius:50%;background:radial-gradient(circle at 50% 45%,#c98a6a,#7a3c2a)}
.btn-logout{background:var(--teal);color:#fff;border-radius:8px;width:91px;height:32px;font-size:15px;display:flex;align-items:center;justify-content:center}
.category-panel{position:absolute;left:99px;top:139px;width:264px;height:415px;background:var(--panel);border-radius:6px;overflow:hidden;box-shadow:0 1px 3px rgba(0,0,0,.04)}
.category-panel h2{background:var(--teal);color:#fff;font-weight:400;font-size:22px;height:49px;line-height:49px;text-align:center}
.category-list{list-style:none;padding:8px 14px 0 18px}
.category-list li{display:flex;justify-content:space-between;height:34px;line-height:34px;font-size:12.5px;border-bottom:1px solid var(--line);padding:0 12px 0 4px}
.category-list li:last-child{border-bottom:none}
.filter-panel{position:absolute;left:420px;top:138px;width:681px;height:90px;background:var(--panel);border-radius:8px;box-shadow:0 1px 3px rgba(0,0,0,.04)}
.field{position:absolute;top:27px;width:218px;height:34px;border:1px solid #e2e2e2;border-radius:8px;font-size:12.5px;color:var(--muted);padding:0 14px;line-height:32px}
.field-keyword{left:53px}
.field-district{left:277px}
.field-district svg{position:absolute;right:14px;top:12px}
.btn-filter{position:absolute;left:509px;top:27px;width:122px;height:33px;background:var(--purple);color:#fff;border-radius:8px;font-size:13px;display:flex;align-items:center;justify-content:center}
.jobs-panel{position:absolute;left:420px;top:246px;width:681px;height:309px;background:var(--panel);border-radius:8px;overflow:hidden;box-shadow:0 1px 3px rgba(0,0,0,.04)}
.job-row{position:absolute;left:0;width:681px;height:49px;font-size:13px;color:var(--text)}
.job-row span{position:absolute;top:50%;transform:translateY(-50%)}
.job-row .c1{left:16px;font-size:15px}
.job-row .c2{left:252px}
.job-row .c3{left:461px}
.job-head{color:var(--purple);font-weight:600}
.job-head .c1{font-size:14.5px}
.job-head .c2,.job-head .c3{font-size:14.5px}
.job-active{background:var(--teal);color:#fff}
.btn-apply{position:absolute;left:594px;top:50%;transform:translateY(-50%);width:73px;height:27px;border-radius:8px;background:var(--blue);color:#fff;font-size:12.5px;display:flex;align-items:center;justify-content:center}
.job-active .btn-apply{background:var(--purple)}
.mascot{position:absolute;left:108px;top:605px;width:200px;height:270px;border-radius:45% 45% 35% 35%;background:radial-gradient(ellipse at 50% 40%,#ececec,rgba(236,236,236,0) 70%)}
.featured-title{position:absolute;left:420px;top:601px;font-size:21px;color:var(--text-dark);font-weight:400}
.provider{position:absolute;top:654px;width:159px;height:124px;background:var(--panel);display:flex;align-items:center;justify-content:center;gap:7px;font-size:15px;font-weight:600;color:var(--text-dark)}
.provider i{width:12px;height:12px;background:var(--teal);display:block}
.rule{position:absolute;left:111px;top:804px;width:990px;border-top:1px dotted #c8c8c8}
.site-footer{position:absolute;top:844px;left:263px;width:838px;display:flex;justify-content:space-between;font-size:11.5px;color:var(--text-dark)}
.site-footer .sep{margin:0 12px}
</style>
</head>
<body>
<div class="top-stripe"><span style="background:var(--stripe-blue)"></span><span style="background:var(--stripe-pink)"></span><span style="background:var(--teal)"></span></div>
<header class="site-header">
  <div class="brand">Velorant <b>Jobs</b></div>
  <nav class="main-nav">About Us<span class="sep">|</span>Contact Us</nav>
  <div class="user-tools">
    <svg width="24" height="24" viewBox="0 0 24 24" aria-label="Search"><circle cx="10" cy="10" r="7" fill="none" stroke="#666" stroke-width="3"/><line x1="15" y1="15" x2="22" y2="22" stroke="#666" stroke-width="3.5" stroke-linecap="round"/></svg>
    <div class="bell">
      <svg width="20" height="22" viewBox="0 0 20 22" aria-label="Notifications"><path d="M10 2a6 6 0 0 0-6 6v5l-2 4h16l-2-4V8a6 6 0 0 0-6-6z" fill="#666"/><circle cx="10" cy="19.5" r="2.3" fill="#666"/></svg>
      <span class="badge">23</span>
    </div>
    <div class="avatar" role="img" aria-label="User profile photo"></div>
    <div class="btn-logout">Logout</div>
  </div>
</header>

<aside class="category-panel">
  <h2>Categories</h2>
  <ul class="category-list">
    <li><span>Category 1</span><span>(33)</span></li>
    <li><span>Category 2</span><span>(3)</span></li>
    <li><span>Category 3</span><span>(324)</span></li>
    <li><span>Category 4</span><span>(45)</span></li>
    <li><span>Category 5</span><span>(56)</span></li>
    <li><span>Category 6</span><span>(3245)</span></li>
    <li><span>Category 7</span><span>(33)</span></li>
    <li><span>Category 8</span><span>(332)</span></li>
    <li><span>Category 9</span><span>(33)</span></li>
  </ul>
</aside>

<section class="filter-panel">
  <div class="field field-keyword">Keyword</div>
  <div class="field field-district">District<svg width="11" height="7" viewBox="0 0 11 7"><path d="M1 1l4.5 4.5L10 1" fill="none" stroke="#999" stroke-width="1.5"/></svg></div>
  <div class="btn-filter">FILTER JOBS</div>
</section>

<section class="jobs-panel">
  <div class="job-row job-head" style="top:12px"><span class="c1">Job Tittle</span><span class="c2">Due Date</span><span class="c3">Provider Name</span></div>
  <div class="job-row job-active" style="top:65px"><span class="c1">Job title number 1</span><span class="c2">Due date 23 jan 2015</span><span class="c3">Provider 1</span><div class="btn-apply">Apply</div></div>
  <div class="job-row" style="top:116px"><span class="c1">Job title number 2</span><span class="c2">Due date 03 jan 2015</span><span class="c3">Provider 3</span><div class="btn-apply">Apply</div></div>
  <div class="job-row" style="top:168px"><span class="c1">Job title number 3</span><span class="c2">Due date 11 jan 2015</span><span class="c3">Provider 2</span><div class="btn-apply">Apply</div></div>
  <div class="job-row" style="top:219px"><span class="c1">Job title number 4</span><span class="c2">Due date 23 jan 2015</span><span class="c3">Provider 1</span><div class="btn-apply">Apply</div></div>
</section>

<div class="mascot" role="img" aria-label="Faint mascot character illustration"></div>

<h3 class="featured-title">Featured Job Providers</h3>
<div class="provider" style="left:421px"><i></i>Northwind Co</div>
<div class="provider" style="left:595px"><i></i>Brightpath</div>
<div class="provider" style="left:770px"><i></i>Lumen Hire</div>
<div class="provider" style="left:944px"><i></i>Corala Studio</div>

<div class="rule"></div>
<footer class="site-footer">
  <span>Copyrights reserved to Velorant Jobs 2015</span>
  <span>About Us<span class="sep">|</span>Terms and conditions<span class="sep">|</span>Sitemap</span>
</footer>
</body>
</html>
```